Scrap Metal Recycling

We are looking for a simple yet bold business card. We already have the logo, please see attached. Color scheme of blue, black and white or just blue and white.

```html
<!DOCTYPE html>
<html lang="en">
<head>
<meta charset="utf-8">
<title>Ridgeline Metals Inc. – Business Card</title>
<link href="https://fonts.googleapis.com/css2?family=Inter:wght@400;500;700;800&display=swap" rel="stylesheet">
<style>
  :root {
    --backdrop: #5b5b5b;
    --charcoal: #3b3b3c;
    --ink: #2a2a2a;
    --text: #4a4a4a;
    --blue: #1a8dba;
    --white: #ffffff;
  }
  * { box-sizing: border-box; margin: 0; padding: 0; }
  html, body { width: 1200px; height: 960px; overflow: hidden; }
  body {
    background: var(--backdrop);
    font-family: "Inter", sans-serif;
    position: relative;
  }
  .card {
    position: absolute;
    width: 620px;
    height: 354px;
    border-radius: 30px;
    overflow: hidden;
    box-shadow: 0 10px 30px rgba(0,0,0,.35);
  }
  .card--front {
    left: 70px; top: 80px;
    background: var(--charcoal);
    display: flex; align-items: center; justify-content: center;
  }
  .brand { display: flex; align-items: center; gap: 16px; }
  .brand__dot {
    width: 22px; height: 22px; border-radius: 50%;
    background: var(--blue);
  }
  .brand__name {
    font-size: 40px; font-weight: 700; color: var(--white);
    letter-spacing: 0.5px;
  }
  .card--back {
    left: 510px; top: 520px;
    background: var(--white);
  }
  .back__decor { position: absolute; right: -90px; top: -60px; }
  .back__tab {
    position: absolute; left: 0; top: 118px;
    width: 12px; height: 36px; background: var(--blue);
  }
  .contact { position: absolute; left: 40px; top: 62px; }
  .contact__name {
    font-size: 26px; font-weight: 800; color: var(--ink);
    letter-spacing: -0.3px; line-height: 1.2;
  }
  .contact__role {
    font-size: 17px; color: var(--blue); font-weight: 500;
    margin-top: 2px; line-height: 1.2;
  }
  .contact__list { list-style: none; margin-top: 14px; }
  .contact__item {
    display: flex; gap: 12px; align-items: flex-start;
    font-size: 15px; color: var(--text); line-height: 1.35;
    margin-bottom: 4px;
  }
  .contact__icon { width: 16px; height: 16px; margin-top: 2px; flex: none; fill: var(--blue); }
  .contact__web {
    margin-top: 10px; margin-left: 28px;
    font-size: 18px; font-weight: 700; color: var(--blue);
    line-height: 1.2;
  }
</style>
</head>
<body>
  <section class="card card--front" aria-label="Card front">
    <div class="brand">
      <span class="brand__dot"></span>
      <span class="brand__name">Ridgeline Metals Inc.</span>
    </div>
  </section>

  <section class="card card--back" aria-label="Card back">
    <svg class="back__decor" width="380" height="380" viewBox="0 0 380 380" aria-hidden="true">
      <circle cx="190" cy="190" r="190" fill="var(--charcoal)"/>
    </svg>
    <span class="back__tab"></span>
    <div class="contact">
      <h1 class="contact__name">DANIEL REYES</h1>
      <p class="contact__role">President</p>
      <ul class="contact__list">
        <li class="contact__item">
          <svg class="contact__icon" viewBox="0 0 16 16"><path d="M8 0a5.5 5.5 0 0 0-5.5 5.5C2.5 10 8 16 8 16s5.5-6 5.5-10.5A5.5 5.5 0 0 0 8 0zm0 8a2.5 2.5 0 1 1 0-5 2.5 2.5 0 0 1 0 5z"/></svg>
          <span>1420 Harbor Road<br>Fairbanks 99701</span>
        </li>
        <li class="contact__item">
          <svg class="contact__icon" viewBox="0 0 16 16"><path d="M3.6 1l2.5 3-1.4 1.7a9 9 0 0 0 5.6 5.6L12 9.9l3 2.5-1.6 2.4C7.4 15 1 8.6 1.2 2.6z"/></svg>
          <span>555-214-0386</span>
        </li>
        <li class="contact__item">
          <svg class="contact__icon" viewBox="0 0 16 16"><path d="M4 0h8a1 1 0 0 1 1 1v14a1 1 0 0 1-1 1H4a1 1 0 0 1-1-1V1a1 1 0 0 1 1-1zm1 2v10h6V2z"/></svg>
          <span>555-318-7742</span>
        </li>
        <li class="contact__item">
          <svg class="contact__icon" viewBox="0 0 16 16"><path d="M4 1h8v4H4zM1 6h14v6h-3v3H4v-3H1zm4 5v3h6v-3z"/></svg>
          <span>555-406-1159</span>
        </li>
        <li class="contact__item">
          <svg class="contact__icon" viewBox="0 0 16 16"><path d="M0 3h16v1L8 9 0 4zm0 3l8 5 8-5v7H0z"/></svg>
          <span>info@ridgelinemetals.com</span>
        </li>
      </ul>
      <p class="contact__web">ridgelinemetals.com</p>
    </div>
  </section>
</body>
</html>
```